Brindlecove Ventures Co. requiresupdated PPT Master

We are a software company that specializes in Business Management solutions for the global Oil and Gas sector. We have an existing logo and color scheme but we would like a new modern twist for our PPT Master template. We would like it to be simple and clean but sophisticated. We would like to reflect both industries on the Title Master Technology and Oil and Gas. We can provide a screen capture of our software if you would like.

Target Market(s)

Oil and Gas Professionals. Various age groups and genders, usually well educated working in Budgeting, Planning, Operations, Finance.

Industry/Entity Type

Software

Requirements
Must have
• Corporate logo and color scheme. RGB 143 Red, 75 Green and 6 Blue. The majority of slides we use are screen captures from our application so we need maximum space. Plus it must be designed to be as small as possible as they are emailed frequently.

```html
<!DOCTYPE html>
<html lang="en">
<head>
<meta charset="utf-8">
<title>Brindlecove – PPT Master</title>
<link rel="stylesheet" href="https://fonts.googleapis.com/css2?family=Jost:wght@400;500;600&display=swap">
<style>
  :root {
    --brand: #8f4b06;
    --stage: #7b7b7b;
    --slide: #f4f4f4;
    --slide-edge: #e6e6e6;
    --band: #dcdcdc;
    --ink: #2b2b2b;
    --muted: #8a8a8a;
    --ui-line: #c9ced6;
    --ui-text: #b9bec6;
    --ui-head: #dde5ef;
    --bar-red: #b8282c;
    --bar-grey: #4a5257;
    --area: #3f5560;
    --gantt: #9a9ae6;
    --cell-green: #3fd36b;
    --cell-yellow: #f3ef6a;
  }
  * { box-sizing: border-box; margin: 0; padding: 0; }
  html, body { width: 1200px; height: 929px; overflow: hidden; }
  body { background: var(--stage); font-family: "Jost", sans-serif; position: relative; }

  .slide {
    position: absolute; width: 576px; height: 434px;
    background: linear-gradient(180deg, #fbfbfb 0%, var(--slide) 70%, var(--slide-edge) 100%);
    overflow: hidden;
  }
  .slide--title { left: 17px; top: 18px; }
  .slide--about { left: 607px; top: 18px; }
  .slide--product { left: 317px; top: 476px; }

  .slide__footer-band { position: absolute; left: 0; right: 0; bottom: 5px; height: 20px; background: var(--band); }
  .slide__footer-rule { position: absolute; left: 0; right: 0; bottom: 0; height: 5px; background: var(--brand); }
  .slide__pumpjack {
    position: absolute; left: 2px; bottom: 22px; width: 78px; height: 58px;
    background: radial-gradient(ellipse at 50% 70%, rgba(0,0,0,0.09) 0%, rgba(0,0,0,0.04) 45%, rgba(0,0,0,0) 72%);
  }

  /* Title slide */
  .title-stripe { position: absolute; left: 79px; top: 0; bottom: 25px; width: 18px; background: linear-gradient(90deg, #e2e2e2, #ffffff 50%, #e2e2e2); }
  .brand-tile {
    position: absolute; left: 97px; top: 168px; width: 78px; height: 94px;
    background: #fff; display: flex; flex-direction: column; align-items: center; justify-content: center; gap: 8px;
    box-shadow: 0 3px 6px rgba(0,0,0,0.25);
  }
  .brand-tile__square { width: 34px; height: 34px; background: var(--brand); }
  .brand-name { color: var(--brand); font-weight: 600; font-size: 13px; }
  .hero-photo { position: absolute; top: 168px; width: 125px; height: 94px; box-shadow: 0 3px 6px rgba(0,0,0,0.25); }
  .hero-photo--refinery { left: 182px; background: linear-gradient(180deg, #5a7aa0 0%, #9fa6b0 30%, #e0a24f 52%, #5a4636 72%, #2c2724 100%); }
  .hero-photo--laptop { left: 314px; background: radial-gradient(circle at 50% 50%, #f4fbfe 0%, #8fd6f1 30%, #2ea3d6 65%, #0f6a9a 100%); }
  .hero-photo--engineer { left: 446px; background: linear-gradient(100deg, #eeeeee 0%, #cfcfcf 35%, #c5362c 55%, #8e1f1a 72%, #3a3a3a 100%); }
  .presentation-title { position: absolute; right: 8px; top: 306px; color: var(--brand); font-weight: 600; font-size: 21px; }
  .presenter-line { position: absolute; right: 8px; top: 335px; color: var(--muted); font-size: 11px; }

  /* Header */
  .slide-header { position: absolute; left: 12px; top: 17px; display: flex; align-items: stretch; }
  .slide-header__mark { width: 40px; display: flex; flex-direction: column; align-items: center; justify-content: center; gap: 2px; }
  .slide-header__square { width: 26px; height: 26px; background: var(--brand); }
  .slide-header__mark .brand-name { font-size: 7px; }
  .slide-header__divider { width: 2px; background: var(--brand); margin: 0 6px 0 2px; }
  .slide-header__title { color: var(--brand); font-weight: 600; font-size: 21px; line-height: 1.1; }
  .slide-header__tagline { color: var(--muted); font-size: 10px; margin-top: 2px; }

  /* About slide */
  .fact-list { position: absolute; left: 70px; top: 100px; list-style: none; color: var(--ink); font-size: 12.5px; line-height: 1.4; width: 480px; }
  .fact-list > li { position: relative; padding-left: 10px; margin-bottom: 15px; }
  .fact-list li::before { content: ""; position: absolute; left: 0; top: 6px; width: 5px; height: 5px; background: var(--brand); }
  .fact-list ul { list-style: none; margin-top: 16px; padding-left: 28px; font-size: 10px; }
  .fact-list ul li { position: relative; padding-left: 9px; margin-bottom: 16px; }
  .fact-list ul li::before { top: 5px; width: 4px; height: 4px; }
  .focus-box {
    position: absolute; left: 93px; top: 314px; width: 403px; height: 62px;
    background: var(--brand); border-radius: 8px; color: #fff;
    display: flex; align-items: center; padding-left: 12px; gap: 10px; font-weight: 500; font-size: 12.5px; line-height: 1.35;
  }

  /* Product slide */
  .app-capture {
    position: absolute; left: 62px; top: 80px; width: 485px; height: 314px;
    background: #fff; box-shadow: 0 3px 8px rgba(0,0,0,0.3);
  }
  .app-capture svg { display: block; }
  .ui-title { font-family: "Jost", sans-serif; font-size: 5px; font-weight: 600; fill: #333; }
</style>
</head>
<body>

<section class="slide slide--title">
  <div class="title-stripe"></div>
  <div class="brand-tile"><span class="brand-tile__square"></span><span class="brand-name">Brindlecove</span></div>
  <div class="hero-photo hero-photo--refinery" role="img" aria-label="Oil refinery at dusk"></div>
  <div class="hero-photo hero-photo--laptop" role="img" aria-label="Laptop on a blue light-burst background"></div>
  <div class="hero-photo hero-photo--engineer" role="img" aria-label="Field engineer in a hard hat using a laptop"></div>
  <h1 class="presentation-title">Presentation Title Goes Here</h1>
  <p class="presenter-line">Presenter Name, 21 May 2013</p>
  <div class="slide__pumpjack" role="img" aria-label="Faint oil pumpjack silhouette"></div>
  <div class="slide__footer-band"></div>
  <div class="slide__footer-rule"></div>
</section>

<section class="slide slide--about">
  <header class="slide-header">
    <div class="slide-header__mark"><span class="slide-header__square"></span><span class="brand-name">Brindlecove</span></div>
    <div class="slide-header__divider"></div>
    <div>
      <h2 class="slide-header__title">Brindlecove – enabling shared intelligence</h2>
      <p class="slide-header__tagline">Subtitle or tagline goes here</p>
    </div>
  </header>
  <ul class="fact-list">
    <li>Started operations in 2006</li>
    <li>HQ in Calgary; Offices in USA, Europe, Latin America &amp; Australia</li>
    <li>Combines a history of successful commercial software (Corvantek) development with solid Oil &amp; Gas industry expertise</li>
    <li>More than 50 installations world-wide
      <ul>
        <li>2 of the top 10 largest Integrated Oil &amp; Gas Companies</li>
        <li>4 of the top 10 largest USA Independent Oil &amp; Gas Companies</li>
      </ul>
    </li>
  </ul>
  <div class="focus-box">
    <span>FOCUS:</span>
    <span>Helping upstream Oil &amp; Gas companies to maximize<br>Value with an Integrated Business Planning process</span>
  </div>
  <div class="slide__pumpjack" role="img" aria-label="Faint oil pumpjack silhouette"></div>
  <div class="slide__footer-band"></div>
  <div class="slide__footer-rule"></div>
</section>

<section class="slide slide--product">
  <header class="slide-header">
    <div class="slide-header__mark"><span class="slide-header__square"></span><span class="brand-name">Brindlecove</span></div>
    <div class="slide-header__divider"></div>
    <div>
      <h2 class="slide-header__title">Our Product</h2>
      <p class="slide-header__tagline">Subtitle or tagline goes here</p>
    </div>
  </header>
  <div class="app-capture" role="img" aria-label="Planning application workspace with project browser, expenditure, production, schedule, ranking and cashflow views">
    <svg width="485" height="314" viewBox="0 0 485 314">
      <!-- window chrome -->
      <rect x="0" y="0" width="485" height="5" fill="#2e3236"/>
      <rect x="0" y="5" width="485" height="7" fill="#eef1f5"/>
      <rect x="3" y="7" width="8" height="2.5" fill="var(--ui-text)"/>
      <rect x="14" y="7" width="10" height="2.5" fill="var(--ui-text)"/>
      <rect x="27" y="7" width="7" height="2.5" fill="var(--ui-text)"/>
      <rect x="0" y="12" width="485" height="8" fill="#e4e9ef"/>
      <rect x="380" y="14" width="100" height="4" fill="var(--ui-text)"/>

      <!-- panels -->
      <g fill="#fff" stroke="var(--ui-line)" stroke-width="0.6">
        <rect x="1" y="21" width="89" height="185"/>
        <rect x="1" y="208" width="89" height="105"/>
        <rect x="92" y="21" width="198" height="80"/>
        <rect x="92" y="103" width="198" height="103"/>
        <rect x="92" y="208" width="198" height="105"/>
        <rect x="292" y="21" width="192" height="80"/>
        <rect x="292" y="103" width="192" height="77"/>
        <rect x="292" y="182" width="192" height="131"/>
      </g>
      <g fill="var(--ui-head)">
        <rect x="1.3" y="21.3" width="88.4" height="5"/>
        <rect x="1.3" y="208.3" width="88.4" height="5"/>
        <rect x="92.3" y="21.3" width="197.4" height="5"/>
        <rect x="92.3" y="103.3" width="197.4" height="5"/>
        <rect x="92.3" y="208.3" width="197.4" height="5"/>
        <rect x="292.3" y="21.3" width="191.4" height="5"/>
        <rect x="292.3" y="103.3" width="191.4" height="5"/>
        <rect x="292.3" y="182.3" width="191.4" height="5"/>
      </g>

      <!-- tree: top left -->
      <g fill="var(--ui-text)">
        <rect x="4" y="30" width="70" height="3" fill="#eef1f5" stroke="var(--ui-line)" stroke-width="0.4"/>
        <rect x="6" y="38" width="20" height="2"/><rect x="10" y="43" width="22" height="2"/>
        <rect x="10" y="48" width="18" height="2"/><rect x="14" y="53" width="24" height="2"/>
        <rect x="18" y="58" width="28" height="2"/><rect x="22" y="63" width="20" height="2"/>
        <rect x="22" y="68" width="16" height="2"/><rect x="22" y="73" width="22" height="2"/>
        <rect x="22" y="78" width="14" height="2"/><rect x="22" y="83" width="24" height="2"/>
        <rect x="22" y="88" width="18" height="2"/><rect x="22" y="93" width="20" height="2"/>
        <rect x="22" y="98" width="16" height="2"/><rect x="22" y="103" width="22" height="2"/>
        <rect x="22" y="108" width="14" height="2"/><rect x="18" y="113" width="26" height="2"/>
        <rect x="22" y="118" width="16" height="2"/><rect x="22" y="123" width="20" height="2"/>
        <rect x="10" y="130" width="18" height="2"/><rect x="10" y="135" width="22" height="2"/>
        <rect x="10" y="140" width="16" height="2"/><rect x="14" y="145" width="22" height="2"/>
        <rect x="18" y="150" width="18" height="2"/><rect x="18" y="155" width="20" height="2"/>
        <rect x="18" y="160" width="24" height="2"/><rect x="10" y="167" width="14" height="2"/>
        <rect x="10" y="172" width="26" height="2"/>
      </g>
      <g fill="#4caf50"><rect x="16" y="57.5" width="3" height="3"/><rect x="6" y="47.5" width="3" height="3"/></g>

      <!-- tree: bottom left -->
      <g fill="var(--ui-text)">
        <rect x="6" y="217" width="20" height="2"/><rect x="10" y="222" width="26" height="2"/>
        <rect x="10" y="227" width="18" height="2"/><rect x="14" y="232" width="22" height="2"/>
        <rect x="14" y="237" width="24" height="2"/><rect x="14" y="242" width="20" height="2"/>
        <rect x="14" y="247" width="22" height="2"/><rect x="10" y="252" width="16" height="2"/>
        <rect x="14" y="257" width="28" height="2"/><rect x="14" y="262" width="24" height="2"/>
        <rect x="14" y="267" width="20" height="2"/><rect x="10" y="272" width="14" height="2"/>
        <rect x="10" y="277" width="18" height="2"/><rect x="10" y="282" width="16" height="2"/>
        <rect x="10" y="287" width="26" height="2"/><rect x="10" y="292" width="18" height="2"/>
      </g>
      <g fill="#e3b341"><rect x="6" y="221.5" width="3" height="3"/><rect x="6" y="251.5" width="3" height="3"/><rect x="6" y="271.5" width="3" height="3"/></g>

      <!-- project browser table -->
      <rect x="95" y="29" width="40" height="3" fill="#5a6b82"/>
      <rect x="170" y="29" width="110" height="3" fill="#9fb2c8"/>
      <rect x="95" y="35" width="192" height="4" fill="#eef1f5" stroke="var(--ui-line)" stroke-width="0.4"/>
      <g fill="var(--ui-text)">
        <rect x="97" y="42" width="20" height="2"/><rect x="125" y="42" width="50" height="2"/><rect x="212" y="42" width="14" height="2"/><rect x="236" y="42" width="18" height="2"/>
        <rect x="97" y="47" width="20" height="2"/><rect x="125" y="47" width="56" height="2"/><rect x="212" y="47" width="14" height="2"/><rect x="236" y="47" width="18" height="2"/>
        <rect x="97" y="52" width="20" height="2"/><rect x="125" y="52" width="46" height="2"/><rect x="212" y="52" width="14" height="2"/><rect x="236" y="52" width="18" height="2"/>
        <rect x="97" y="57" width="20" height="2"/><rect x="125" y="57" width="60" height="2"/><rect x="212" y="57" width="14" height="2"/><rect x="236" y="57" width="18" height="2"/>
        <rect x="97" y="62" width="20" height="2"/><rect x="125" y="62" width="52" height="2"/><rect x="212" y="62" width="14" height="2"/><rect x="236" y="62" width="18" height="2"/>
        <rect x="97" y="67" width="20" height="2"/><rect x="125" y="67" width="48" height="2"/><rect x="212" y="67" width="14" height="2"/><rect x="236" y="67" width="18" height="2"/>
      </g>

      <!-- expenditure chart -->
      <text class="ui-title" x="186" y="121">Expenditure</text>
      <g stroke="#e4e4e4" stroke-width="0.4">
        <line x1="115" y1="130" x2="270" y2="130"/><line x1="115" y1="145" x2="270" y2="145"/>
        <line x1="115" y1="160" x2="270" y2="160"/><line x1="115" y1="175" x2="270" y2="175"/>
      </g>
      <line x1="115" y1="188" x2="270" y2="188" stroke="#888" stroke-width="0.5"/>
      <g fill="var(--bar-red)">
        <rect x="120" y="158" width="3.5" height="30"/><rect x="130" y="148" width="3.5" height="40"/>
        <rect x="140" y="150" width="3.5" height="38"/><rect x="150" y="143" width="3.5" height="45"/>
        <rect x="160" y="146" width="3.5" height="42"/><rect x="170" y="138" width="3.5" height="50"/>
        <rect x="180" y="141" width="3.5" height="47"/><rect x="190" y="144" width="3.5" height="44"/>
        <rect x="200" y="140" width="3.5" height="48"/><rect x="210" y="136" width="3.5" height="52"/>
        <rect x="220" y="142" width="3.5" height="46"/><rect x="230" y="139" width="3.5" height="49"/>
        <rect x="240" y="145" width="3.5" height="43"/><rect x="250" y="148" width="3.5" height="40"/>
      </g>
      <g fill="var(--bar-grey)">
        <rect x="124" y="153" width="3.5" height="35"/><rect x="134" y="144" width="3.5" height="44"/>
        <rect x="144" y="142" width="3.5" height="46"/><rect x="154" y="138" width="3.5" height="50"/>
        <rect x="164" y="140" width="3.5" height="48"/><rect x="174" y="133" width="3.5" height="55"/>
        <rect x="184" y="136" width="3.5" height="52"/><rect x="194" y="139" width="3.5" height="49"/>
        <rect x="204" y="134" width="3.5" height="54"/><rect x="214" y="132" width="3.5" height="56"/>
        <rect x="224" y="138" width="3.5" height="50"/><rect x="234" y="135" width="3.5" height="53"/>
        <rect x="244" y="141" width="3.5" height="47"/><rect x="254" y="143" width="3.5" height="45"/>
      </g>
      <rect x="274" y="155" width="4" height="3" fill="var(--bar-grey)"/><rect x="274" y="160" width="4" height="3" fill="var(--bar-red)"/>

      <!-- production chart -->
      <text class="ui-title" x="188" y="226">Production</text>
      <line x1="110" y1="295" x2="265" y2="295" stroke="#888" stroke-width="0.5"/>
      <path d="M110 295 L110 288 L125 282 L140 268 L160 262 L180 258 L195 253 L215 260 L235 266 L250 271 L262 276 L262 295 Z" fill="var(--area)"/>
      <path d="M110 295 L110 288 L118 285 L122 270 L126 280 L126 295 Z" fill="var(--bar-red)"/>
      <rect x="270" y="270" width="4" height="3" fill="var(--area)"/><rect x="270" y="275" width="4" height="3" fill="var(--bar-red)"/>

      <!-- schedule / gantt -->
      <rect x="340" y="29" width="140" height="6" fill="#eef1f5" stroke="var(--ui-line)" stroke-width="0.4"/>
      <g stroke="#e0e0e0" stroke-width="0.4">
        <line x1="340" y1="40" x2="480" y2="40"/><line x1="340" y1="47" x2="480" y2="47"/>
        <line x1="340" y1="54" x2="480" y2="54"/><line x1="340" y1="61" x2="480" y2="61"/>
        <line x1="340" y1="68" x2="480" y2="68"/><line x1="340" y1="75" x2="480" y2="75"/>
        <line x1="340" y1="82" x2="480" y2="82"/><line x1="340" y1="89" x2="480" y2="89"/>
        <line x1="360" y1="35" x2="360" y2="96"/><line x1="380" y1="35" x2="380" y2="96"/>
        <line x1="400" y1="35" x2="400" y2="96"/><line x1="420" y1="35" x2="420" y2="96"/>
        <line x1="440" y1="35" x2="440" y2="96"/><line x1="460" y1="35" x2="460" y2="96"/>
      </g>
      <g fill="var(--ui-text)">
        <rect x="296" y="41" width="36" height="2"/><rect x="300" y="48" width="30" height="2"/>
        <rect x="300" y="55" width="32" height="2"/><rect x="296" y="62" width="36" height="2"/>
        <rect x="300" y="69" width="30" height="2"/><rect x="296" y="76" width="34" height="2"/>
        <rect x="300" y="83" width="30" height="2"/><rect x="296" y="90" width="36" height="2"/>
      </g>
      <g fill="var(--gantt)">
        <rect x="392" y="41" width="10" height="3"/><rect x="354" y="55" width="24" height="3"/>
        <rect x="372" y="62" width="14" height="3"/><rect x="380" y="83" width="40" height="3"/>
      </g>
      <rect x="352" y="64" width="34" height="20" fill="#fbf7c8" stroke="#c9c28a" stroke-width="0.4"/>
      <g fill="#a8a07a"><rect x="355" y="68" width="22" height="1.6"/><rect x="355" y="73" width="26" height="1.6"/><rect x="355" y="78" width="24" height="1.6"/></g>

      <!-- ranking table -->
      <rect x="296" y="111" width="40" height="2.5" fill="#7aa4c8"/>
      <rect x="296" y="118" width="184" height="5" fill="#eef1f5" stroke="var(--ui-line)" stroke-width="0.4"/>
      <g fill="var(--ui-text)">
        <rect x="306" y="126" width="40" height="2"/><rect x="306" y="131" width="44" height="2"/>
        <rect x="306" y="136" width="38" height="2"/><rect x="306" y="141" width="42" height="2"/>
      </g>
      <g fill="var(--cell-yellow)">
        <rect x="372" y="125" width="20" height="4"/><rect x="372" y="135" width="20" height="4"/><rect x="372" y="140" width="20" height="4"/>
      </g>
      <g fill="var(--cell-green)">
        <rect x="394" y="125" width="18" height="4"/><rect x="414" y="125" width="20" height="4"/><rect x="436" y="125" width="18" height="4"/>
        <rect x="372" y="130" width="20" height="4"/><rect x="394" y="130" width="18" height="4"/><rect x="414" y="130" width="20" height="4"/><rect x="436" y="130" width="18" height="4"/>
        <rect x="394" y="135" width="18" height="4"/><rect x="414" y="135" width="20" height="4"/><rect x="436" y="135" width="18" height="4"/>
        <rect x="394" y="140" width="18" height="4"/><rect x="414" y="140" width="20" height="4"/><rect x="436" y="140" width="18" height="4"/>
      </g>
      <rect x="296" y="166" width="30" height="2" fill="#7aa4c8"/>

      <!-- cashflow chart -->
      <rect x="372" y="190" width="40" height="2.5" fill="#555"/>
      <g stroke="#e4e4e4" stroke-width="0.4">
        <line x1="305" y1="205" x2="460" y2="205"/><line x1="305" y1="225" x2="460" y2="225"/>
        <line x1="305" y1="245" x2="460" y2="245"/><line x1="305" y1="265" x2="460" y2="265"/>
      </g>
      <line x1="305" y1="285" x2="460" y2="285" stroke="#888" stroke-width="0.5"/>
      <g fill="none" stroke="var(--bar-red)" stroke-width="0.8">
        <rect x="308" y="265" width="3" height="20"/><rect x="317.5" y="258" width="3" height="27"/>
        <rect x="327" y="252" width="3" height="33"/><rect x="336.5" y="246" width="3" height="39"/>
        <rect x="346" y="241" width="3" height="44"/><rect x="355.5" y="236" width="3" height="49"/>
        <rect x="365" y="231" width="3" height="54"/><rect x="374.5" y="227" width="3" height="58"/>
        <rect x="384" y="223" width="3" height="62"/><rect x="393.5" y="219" width="3" height="66"/>
        <rect x="403" y="215" width="3" height="70"/><rect x="412.5" y="212" width="3" height="73"/>
        <rect x="422" y="209" width="3" height="76"/><rect x="431.5" y="206" width="3" height="79"/>
        <rect x="441" y="203" width="3" height="82"/><rect x="450.5" y="200" width="3" height="85"/>
      </g>
      <g fill="var(--bar-grey)">
        <rect x="312" y="270" width="2.5" height="15"/><rect x="321.5" y="265" width="2.5" height="20"/>
        <rect x="331" y="260" width="2.5" height="25"/><rect x="340.5" y="255" width="2.5" height="30"/>
        <rect x="350" y="251" width="2.5" height="34"/><rect x="359.5" y="247" width="2.5" height="38"/>
        <rect x="369" y="243" width="2.5" height="42"/><rect x="378.5" y="240" width="2.5" height="45"/>
        <rect x="388" y="237" width="2.5" height="48"/><rect x="397.5" y="234" width="2.5" height="51"/>
        <rect x="407" y="231" width="2.5" height="54"/><rect x="416.5" y="229" width="2.5" height="56"/>
        <rect x="426" y="227" width="2.5" height="58"/><rect x="435.5" y="225" width="2.5" height="60"/>
        <rect x="445" y="223" width="2.5" height="62"/><rect x="454.5" y="221" width="2.5" height="64"/>
      </g>
      <rect x="466" y="250" width="4" height="3" fill="var(--bar-grey)"/><rect x="466" y="255" width="4" height="3" fill="var(--bar-red)"/>
    </svg>
  </div>
  <div class="slide__pumpjack" role="img" aria-label="Faint oil pumpjack silhouette"></div>
  <div class="slide__footer-band"></div>
  <div class="slide__footer-rule"></div>
</section>

</body>
</html>
```